Bridal show post card design

our company contracts hotels near airports and cruise ports. We sell hotel packages including one night stay at a hotel (before or after the trip) including parking while they are away and transfers to and from the airport or cruise port. we are marketing to the public for the first time (typically it's travel agents). Specifically doing a Bridal show. Below are the photos that will appear in our booth or on our banners etc. We would like a post card to reflect the stress of not booking a hotel with us ... instead they could start their honeymoon or vacation a day early, stay at the hotel and relax... avoiding the stress of getting to the airport or cruise port in time otherwise missing the boat or the flight. We would also like to include a $20 off savings on the post card.
Industry/Entity Type
Hotel

```html
<!DOCTYPE html>
<html lang="en">
<head>
<meta charset="utf-8">
<title>Harborline Stay &amp; Park – Bridal Show Postcard</title>
<link rel="stylesheet" href="https://fonts.googleapis.com/css2?family=Arimo:wght@400;700&display=swap">
<style>
  :root {
    --navy: #2b2f5c;
    --green: #5d8b3d;
    --green-light: #b3d494;
    --header-top: #f4f4f4;
    --header-bottom: #dedede;
    --ink: #2b2f5c;
    --gray: #555a60;
    --white: #ffffff;
  }
  * { box-sizing: border-box; margin: 0; padding: 0; }
  html, body { width: 1200px; height: 953px; overflow: hidden; background: var(--white); }
  body { font-family: "Arimo", Arial, sans-serif; }

  .postcard { position: relative; width: 1200px; height: 953px; background: var(--white); }

  .brand-header {
    position: absolute; left: 0; top: 0; width: 1200px; height: 207px;
    background: linear-gradient(var(--header-top), var(--header-bottom));
    display: flex; flex-direction: column; align-items: center; justify-content: center;
  }
  .brand-name { font-size: 54px; font-weight: 700; color: var(--navy); letter-spacing: 0.5px; }
  .brand-phone { margin-top: 10px; font-size: 30px; font-weight: 700; color: var(--gray); letter-spacing: 1px; }

  .photo-strip {
    position: absolute; left: 0; top: 213px; width: 1200px; height: 270px;
    display: flex; gap: 9px;
  }
  .photo { flex: 1; height: 100%; }
  .photo--shuttle { background: linear-gradient(135deg, #1b1a1f 10%, #6b3b12 55%, #d7862a 100%); }
  .photo--paris { background: linear-gradient(180deg, #3c5a86 0%, #c58a58 60%, #f2c07a 80%, #3a2a22 100%); }
  .photo--relax { background: linear-gradient(160deg, #e6cfae 0%, #caa47a 60%, #b08a62 100%); }
  .photo--beach { background: linear-gradient(170deg, #9fc3e3 0%, #e9f0f6 55%, #d8d2c6 100%); }

  .benefits {
    position: absolute; left: 0; top: 483px; width: 1200px; height: 204px;
    background: var(--green); display: flex;
  }
  .benefit { flex: 1; display: flex; flex-direction: column; align-items: center; padding-top: 24px; color: var(--white); text-align: center; }
  .benefit-icon { height: 64px; display: flex; align-items: center; }
  .benefit-title { margin-top: 10px; font-size: 30px; font-weight: 400; letter-spacing: 0.5px; }
  .benefit-text { margin-top: 4px; font-size: 19px; line-height: 1.25; }

  .divider-band { position: absolute; left: 0; top: 687px; width: 1200px; height: 11px; background: var(--navy); }

  .offer { position: absolute; left: 0; top: 698px; width: 1200px; height: 255px; }
  .offer-amount {
    position: absolute; left: 90px; top: 36px; width: 260px;
    text-align: center; color: var(--navy); font-weight: 700; line-height: 1;
  }
  .offer-enjoy { font-size: 38px; }
  .offer-value { font-size: 84px; margin-top: 6px; }
  .offer-off { font-size: 60px; margin-top: 2px; }
  .offer-rule { position: absolute; left: 385px; top: 22px; width: 2px; height: 190px; background: var(--navy); }
  .offer-detail {
    position: absolute; left: 410px; top: 50px; width: 400px;
    text-align: center; color: var(--navy); font-size: 34px; line-height: 1.32;
  }
  .offer-detail strong { font-weight: 700; }
  .offer-note { font-size: 24px; font-weight: 700; }
  .offer-art {
    position: absolute; left: 955px; top: 24px; width: 215px; height: 200px;
    border-radius: 50%;
    background: radial-gradient(circle at 55% 55%, #3d8fd0 0%, #2a6db0 45%, #7cbf4a 70%, rgba(255,255,255,0) 72%);
  }
</style>
</head>
<body>
<main class="postcard">
  <header class="brand-header">
    <div class="brand-name">Harborline Stay &amp; Park</div>
    <div class="brand-phone">800-555-0142</div>
  </header>

  <section class="photo-strip">
    <div class="photo photo--shuttle" role="img" aria-label="Glowing airport shuttle sign at night"></div>
    <div class="photo photo--paris" role="img" aria-label="Couple embracing at sunset before the Eiffel Tower"></div>
    <div class="photo photo--relax" role="img" aria-label="The word relax written in beach sand"></div>
    <div class="photo photo--beach" role="img" aria-label="Couple lounging in beach chairs by the sea"></div>
  </section>

  <section class="benefits">
    <div class="benefit">
      <div class="benefit-icon">
        <svg width="90" height="50" viewBox="0 0 90 50" fill="var(--green-light)">
          <path d="M8 30 Q10 20 22 18 L30 6 Q34 2 42 2 L60 2 Q68 2 72 10 L78 18 Q88 20 88 30 L88 38 L8 38 Z"/>
          <circle cx="26" cy="40" r="9" fill="var(--green)"/><circle cx="26" cy="40" r="6"/>
          <circle cx="70" cy="40" r="9" fill="var(--green)"/><circle cx="70" cy="40" r="6"/>
        </svg>
      </div>
      <div class="benefit-title">PARK</div>
      <div class="benefit-text">leave your car at<br>the hotel</div>
    </div>
    <div class="benefit">
      <div class="benefit-icon">
        <svg width="80" height="56" viewBox="0 0 80 56" fill="var(--green-light)">
          <rect x="4" y="4" width="6" height="48"/>
          <rect x="70" y="18" width="6" height="34"/>
          <rect x="10" y="30" width="60" height="12"/>
          <rect x="14" y="18" width="16" height="10" rx="3"/>
          <rect x="32" y="20" width="38" height="10" rx="3"/>
        </svg>
      </div>
      <div class="benefit-title">RELAX</div>
      <div class="benefit-text">start your vacation<br>a night early</div>
    </div>
    <div class="benefit">
      <div class="benefit-icon">
        <svg width="150" height="56" viewBox="0 0 150 56" fill="var(--green-light)">
          <path d="M4 30 L30 26 L40 6 L47 6 L42 25 L58 23 L64 15 L68 15 L66 27 L68 39 L64 39 L58 31 L42 29 L47 48 L40 48 L30 30 Z"/>
          <path d="M82 36 L148 36 L138 50 L90 50 Z"/>
          <rect x="94" y="26" width="40" height="8"/>
          <rect x="104" y="16" width="22" height="8"/>
          <rect x="110" y="8" width="6" height="8"/>
        </svg>
      </div>
      <div class="benefit-title">SHUTTLE</div>
      <div class="benefit-text">transfers to the airport<br>or cruise port</div>
    </div>
    <div class="benefit">
      <div class="benefit-icon">
        <svg width="70" height="60" viewBox="0 0 70 60" fill="var(--green-light)">
          <path d="M8 22 Q32 -2 62 18 Z"/>
          <rect x="33" y="14" width="3" height="44"/>
          <path d="M12 40 L40 40 L48 30 L51 32 L44 42 L44 56 L40 56 L40 46 L18 46 L18 56 L14 56 L14 46 Z"/>
        </svg>
      </div>
      <div class="benefit-title">ENJOY!</div>
      <div class="benefit-text">have a worry<br>free vacation</div>
    </div>
  </section>

  <div class="divider-band"></div>

  <section class="offer">
    <div class="offer-amount">
      <div class="offer-enjoy">ENJOY</div>
      <div class="offer-value">$20</div>
      <div class="offer-off">OFF</div>
    </div>
    <div class="offer-rule"></div>
    <div class="offer-detail">
      A <strong>ONE NIGHT STAY</strong> AT<br>
      ANY OF OUR PROPERTIES<br>
      <span class="offer-note">with this postcard</span>
    </div>
    <div class="offer-art" role="img" aria-label="Globe with palm trees and hotel towers"></div>
  </section>
</main>
</body>
</html>
```